Brindlecove Ventures Co. requiresupdated PPT Master

We are a software company that specializes in Business Management solutions for the global Oil and Gas sector. We have an existing logo and color scheme but we would like a new modern twist for our PPT Master template. We would like it to be simple and clean but sophisticated. We would like to reflect both industries on the Title Master Technology and Oil and Gas. We can provide a screen capture of our software if you would like.

Target Market(s)

Oil and Gas Professionals. Various age groups and genders, usually well educated working in Budgeting, Planning, Operations, Finance.

Industry/Entity Type

Software

Requirements
Must have
• Corporate logo and color scheme. RGB 143 Red, 75 Green and 6 Blue. The majority of slides we use are screen captures from our application so we need maximum space. Plus it must be designed to be as small as possible as they are emailed frequently.

```html
<!DOCTYPE html>
<html lang="en">
<head>
<meta charset="utf-8">
<title>Project Title Here</title>
<link rel="stylesheet" href="https://fonts.googleapis.com/css2?family=Questrial&family=Mulish:wght@400;700&family=Carlito&display=swap">
<style>
  :root {
    --brand-brown: #8f4b06;
    --title-brown: #8a4a0c;
    --footer-rule: #1a1a1a;
    --header-rule: #c9d6dc;
    --page-bg: #fcfcfc;
    --text-dark: #2a2a2a;
    --placeholder-border: #e2e2e2;
    --placeholder-text: #555555;
    --white: #ffffff;
  }
  * { margin: 0; padding: 0; box-sizing: border-box; }
  html, body { width: 1200px; height: 900px; overflow: hidden; background: var(--page-bg); }
  .slide { position: relative; width: 1200px; height: 900px; background: var(--page-bg); overflow: hidden; }

  .header-texture {
    position: absolute; left: 0; top: 0; width: 760px; height: 96px;
    background: linear-gradient(90deg, #ececec 0%, #f5f5f5 45%, rgba(252,252,252,0) 100%);
  }
  .slide-title {
    position: absolute; left: 66px; top: 30px;
    font-family: "Questrial", sans-serif; font-size: 36px; color: var(--title-brown);
    font-weight: 400; letter-spacing: 0.3px;
  }
  .brand {
    position: absolute; right: 12px; top: 20px;
    display: flex; align-items: center; gap: 8px;
    font-family: "Mulish", sans-serif; font-weight: 700; font-size: 17px; color: var(--brand-brown);
  }
  .brand-mark { width: 14px; height: 14px; background: var(--brand-brown); }
  .header-rule {
    position: absolute; left: 0; top: 97px; width: 1200px; height: 2px; background: var(--header-rule);
  }

  .content { position: absolute; left: 71px; top: 156px; width: 600px; font-family: "Mulish", sans-serif; color: var(--text-dark); }
  .section { margin-bottom: 30px; }
  .section-heading { font-weight: 700; font-size: 19px; line-height: 42px; white-space: nowrap; }
  .section-line { font-size: 19px; line-height: 42px; white-space: nowrap; }

  .photo-slot {
    position: absolute; left: 716px; width: 448px; height: 198px;
    border: 2px solid var(--placeholder-border); border-radius: 6px;
    background: var(--white);
    box-shadow: inset 0 0 0 4px #f6f6f6;
    display: flex; align-items: center; justify-content: center;
    font-family: "Carlito", sans-serif; font-size: 21px; color: var(--placeholder-text);
  }
  .photo-slot.top { top: 166px; }
  .photo-slot.bottom { top: 436px; }

  .footer-rule { position: absolute; left: 0; top: 861px; width: 1200px; height: 4px; background: var(--footer-rule); }
  .footer {
    position: absolute; left: 0; top: 865px; width: 1200px; height: 35px; background: var(--brand-brown);
    display: flex; align-items: center; justify-content: space-between; padding: 0 14px 0 34px;
    color: var(--white); font-size: 17px;
  }
  .page-number { font-family: "Carlito", sans-serif; font-weight: 700; }
  .copyright { font-family: "Questrial", sans-serif; }
</style>
</head>
<body>
<main class="slide">
  <div class="header-texture" role="img" aria-label="Faint dotted texture behind the slide header"></div>
  <h1 class="slide-title">Project Title Here</h1>
  <div class="brand"><span class="brand-mark"></span><span>Brindlecove</span></div>
  <div class="header-rule"></div>

  <section class="content">
    <div class="section">
      <p class="section-heading">Lorem ipsum dolor sit ipsum</p>
      <p class="section-line">Lorem ipsum dolor sit ipsum Lorem ipsum dolor sit ipsum</p>
      <p class="section-line">Lorem ipsum dolor sit ipsum Lorem ipsum dolor sit ipsum</p>
      <p class="section-line">Lorem ipsum dolor sit ipsum Lorem ipsum</p>
    </div>
    <div class="section">
      <p class="section-heading">Lorem ipsum dolor sit ipsum Lorem</p>
      <p class="section-line">ipsum dolor sit ipsum Lorem ipsum dolor sit ipsum Lorem</p>
      <p class="section-line">ipsum dolor sit ipsum Lorem ipsum dolor sit ipsum Lorem</p>
      <p class="section-line">ipsum dolor sit ipsum Lorem ipsum dolor sit ipsum Lorem</p>
      <p class="section-line">ipsum dolor sit ipsum</p>
    </div>
    <div class="section">
      <p class="section-heading">Lorem ipsum dolor sit ipsum Lorem</p>
      <p class="section-line">Lorem ipsum dolor sit ipsum Lorem ipsum dolor sit ipsum</p>
      <p class="section-line">Lorem ipsum dolor sit ipsum Lorem ipsum dolor sit ipsum</p>
      <p class="section-line">Lorem ipsum dolor sit ipsum Lorem ipsum dolor sit ipsum</p>
      <p class="section-line">Lorem ipsum dolor sit ipsum Lorem ipsum dolor sit ipsum</p>
    </div>
  </section>

  <div class="photo-slot top">Photo Here</div>
  <div class="photo-slot bottom">Photo Here</div>

  <div class="footer-rule"></div>
  <footer class="footer">
    <span class="page-number">Page : 01</span>
    <span class="copyright">Copyright text here</span>
  </footer>
</main>
</body>
</html>
```